Packaging for New Supplement Line

Need a cool, military themed package designed for new supplement line inspired by a retired Navy Seal. Maybe use KRT Mark II camo (example attached) as background and military fonts - just a suggestion maybe you have a way cooler idea? Product name is "DXRT Core Vanguard"
Navy Seal has a logo we'd like featured somewhere small or not "loud" on the package (example attached) Product to be packaged in a "wide mouth" pouch (example attached) but want a small window to view the contents. Contents will be a special vanilla protein powder in clear stickpacks (example attached) The design should reflect military strength cutting edge, superior nutrition.

```html
<!DOCTYPE html>
<html lang="en">
<head>
<meta charset="utf-8">
<title>DXRT Core Vanguard – Pouch Front</title>
<link href="https://fonts.googleapis.com/css2?family=Russo+One&display=swap" rel="stylesheet">
<style>
  :root {
    --page: #ffffff;
    --camo-tan: #d8c3a0;
    --camo-deep: #b89a72;
    --label-light: #ede1c7;
    --label-mid: #e2d2b2;
    --ink-brown: #654a2e;
    --accent-tan: #b8976c;
    --gold-line: #b9996d;
    --window-brown: #6a4e31;
  }
  * { margin: 0; padding: 0; box-sizing: border-box; }
  html, body {
    width: 1200px; height: 750px; overflow: hidden;
    background: var(--page);
    font-family: "Russo One", sans-serif;
  }
  .pouch-front {
    position: absolute; left: 120px; top: 45px;
    width: 960px; height: 660px;
  }
  .pouch-art { position: absolute; inset: 0; }
  .brand-mark {
    position: absolute; left: 110px; top: 355px;
    display: flex; align-items: center; gap: 10px;
    color: var(--ink-brown); font-size: 22px; letter-spacing: 2px;
  }
  .brand-mark .dot {
    width: 14px; height: 14px; border-radius: 50%;
    background: var(--ink-brown);
  }
  .product-title {
    position: absolute; left: 384px; top: 246px; width: 540px;
    color: var(--ink-brown); text-align: right;
    font-size: 82px; line-height: 76px; letter-spacing: 6px;
    text-transform: uppercase;
  }
  .product-code {
    position: absolute; left: 614px; top: 394px; width: 300px;
    color: var(--accent-tan); font-size: 64px; line-height: 64px;
    letter-spacing: 4px; font-style: normal;
  }
  .features {
    position: absolute; left: 431px; top: 512px; width: 452px;
    display: flex; border-bottom: 2px solid var(--gold-line);
    padding-bottom: 6px;
  }
  .features li {
    list-style: none; flex: 1; text-align: center;
    color: var(--ink-brown); font-size: 13px; line-height: 14px;
    padding: 2px 4px;
  }
  .features li + li { border-left: 2px solid var(--gold-line); }
  .net-content {
    position: absolute; left: 431px; top: 566px; width: 452px;
    text-align: center; color: var(--ink-brown); font-size: 13px;
  }
</style>
</head>
<body>
<main class="pouch-front">
  <svg class="pouch-art" width="960" height="660" viewBox="0 0 960 660">
    <defs>
      <linearGradient id="label-fill" x1="0" y1="0" x2="1" y2="1">
        <stop offset="0" stop-color="var(--label-light)"/>
        <stop offset="1" stop-color="var(--label-mid)"/>
      </linearGradient>
      <linearGradient id="camo-fill" x1="0" y1="0" x2="1" y2="1">
        <stop offset="0" stop-color="var(--camo-tan)"/>
        <stop offset="0.5" stop-color="var(--camo-deep)"/>
        <stop offset="1" stop-color="var(--camo-tan)"/>
      </linearGradient>
    </defs>
    <rect class="label-field" x="0" y="0" width="960" height="660" fill="url(#label-fill)"
          role="img" aria-label="Faint desert digital camouflage pattern"/>
    <path class="camo-band" d="M0 0 H960 V178 H540 C420 178 330 296 220 296 H0 Z"
          fill="url(#camo-fill)" role="img" aria-label="Desert digital camouflage pattern"/>
    <path class="camo-edge" d="M0 296 H220 C330 296 420 178 540 178 H960"
          fill="none" stroke="var(--gold-line)" stroke-width="8"/>
    <g class="speed-stripes" fill="var(--ink-brown)">
      <rect x="414" y="408" width="3" height="42" opacity="0.25"/>
      <rect x="428" y="408" width="4" height="42" opacity="0.3"/>
      <rect x="443" y="408" width="5" height="42" opacity="0.4"/>
      <rect x="459" y="408" width="6" height="42" opacity="0.5"/>
      <rect x="476" y="408" width="7" height="42" opacity="0.6"/>
      <rect x="494" y="408" width="8" height="42" opacity="0.7"/>
      <rect x="513" y="408" width="9" height="42" opacity="0.8"/>
      <rect x="533" y="408" width="10" height="42" opacity="0.9"/>
      <rect x="554" y="408" width="11" height="42"/>
      <rect x="576" y="408" width="12" height="42"/>
      <rect x="596" y="408" width="10" height="42"/>
    </g>
    <rect class="view-window" x="30" y="448" width="350" height="152" rx="28"
          fill="var(--window-brown)"/>
    <rect class="base-band" x="0" y="636" width="960" height="6" fill="var(--gold-line)"/>
  </svg>

  <div class="brand-mark"><span class="dot"></span>IRONTIDE</div>

  <h1 class="product-title">Core<br>Vanguard</h1>
  <div class="product-code">DXRT</div>

  <ul class="features">
    <li>PROBIOTICS<br>VITAMIN D</li>
    <li>5.9G OF BCAAS<br>GLUTEN FREE</li>
    <li>BANNED<br>SUBSTANCE FREE</li>
  </ul>
  <p class="net-content">2.51 KG/ 33 SERVES/ DIETARY SUPPLEMENT</p>
</main>
</body>
</html>
```